kf novum
My service company has specialists in Sales, Marketing and Change Management. Our target group is the 1st and 2nd management level of enterprises, who want to align their strategy at new market situations or to change their distribution, communication or product concept.
We help our clients in defined time frames or projects not only in defining new strategies and concepts but also in implementation and measurements of the results.
I'm looking for a design of business cards and A4 letter paper. The company name is "kf novum"; my name ist Konrad Fels...
So the name of my company stands for Management on time (kf novum) and kf stands for my name (initials)
Logo see enclosed.

```html
<!DOCTYPE html>
<html lang="de">
<head>
<meta charset="utf-8">
<title>kf novum – Briefbogen</title>
<link rel="stylesheet" href="https://fonts.googleapis.com/css2?family=Jura:wght@400;500;700&display=swap">
<style>
  :root {
    --backdrop: #77787a;
    --paper: #ffffff;
    --ink: #3b3e45;
    --ink-dark: #22262e;
    --rule: #a9abae;
  }
  html, body {
    margin: 0;
    padding: 0;
    width: 900px;
    height: 1200px;
    overflow: hidden;
    background: var(--backdrop);
    font-family: "Jura", "Helvetica Neue", Arial, sans-serif;
    color: var(--ink);
  }
  .sheet {
    position: absolute;
    left: 56px;
    top: 43px;
    width: 787px;
    height: 1114px;
    background: var(--paper);
  }
  .side-rule {
    position: absolute;
    left: 524px;
    width: 1px;
    background: var(--rule);
  }
  .side-rule--head { top: 32px; height: 292px; }
  .side-rule--foot { top: 1007px; height: 86px; }

  .brand {
    position: absolute;
    left: 536px;
    top: 122px;
    display: flex;
    align-items: center;
    gap: 11px;
    font-size: 36px;
    font-weight: 500;
    letter-spacing: 0.5px;
    color: var(--ink-dark);
    line-height: 1;
  }
  .brand__dot {
    width: 20px;
    height: 20px;
    border-radius: 50%;
    background: var(--ink-dark);
  }

  .sender-line {
    position: absolute;
    left: 93px;
    top: 228px;
    font-size: 9px;
    letter-spacing: 0.4px;
    color: var(--ink);
  }

  .contact {
    position: absolute;
    left: 537px;
    top: 182px;
    font-style: normal;
    font-size: 12px;
    letter-spacing: 1px;
    line-height: 16px;
  }
  .contact__row {
    display: flex;
    align-items: center;
    gap: 8px;
  }
  .contact__icon {
    width: 9px;
    height: 11px;
    flex: none;
    fill: var(--ink-dark);
  }
  .contact__indent { padding-left: 17px; }
  .contact__name { font-weight: 700; color: var(--ink-dark); }
  .contact__group { margin-top: 5px; }

  .fold-mark {
    position: absolute;
    left: 9px;
    width: 11px;
    height: 1px;
    background: var(--ink-dark);
  }

  .bank {
    position: absolute;
    left: 537px;
    top: 1017px;
    font-size: 11.5px;
    letter-spacing: 1.1px;
    line-height: 16px;
  }
  .bank__codes { margin-top: 5px; }
  .bank__label { display: inline-block; width: 37px; }
</style>
</head>
<body>
  <main class="sheet">
    <div class="side-rule side-rule--head"></div>

    <div class="brand">
      <span class="brand__dot"></span>
      <span class="brand__name">kf novum</span>
    </div>

    <div class="sender-line">kf novum · Musterstraße 12 · 12345 Musterstadt</div>

    <address class="contact">
      <div class="contact__row">
        <svg class="contact__icon" viewBox="0 0 10 13"><path d="M5 0a4.5 4.5 0 0 0-4.5 4.5C.5 8 5 13 5 13s4.5-5 4.5-8.5A4.5 4.5 0 0 0 5 0zm0 6.3a1.8 1.8 0 1 1 0-3.6 1.8 1.8 0 0 1 0 3.6z"/></svg>
        <span class="contact__name">kf novum</span>
      </div>
      <div class="contact__indent">Konrad Fels</div>
      <div class="contact__indent">Musterstrasse 12</div>
      <div class="contact__indent">12345 Musterstadt</div>

      <div class="contact__group">
        <div class="contact__row">
          <svg class="contact__icon" viewBox="0 0 10 12"><path d="M2.2 0.5 4 3.2 2.9 4.4c.5 1.6 1.5 3 2.8 4l1.3-.9L9.3 9.4 8 11.5C4 10.8.6 6.3 1 1.5z"/></svg>
          <span>+49 5550 2468013</span>
        </div>
        <div class="contact__row">
          <svg class="contact__icon" viewBox="0 0 8 12"><path d="M1.2 0h5.6A1.2 1.2 0 0 1 8 1.2v9.6A1.2 1.2 0 0 1 6.8 12H1.2A1.2 1.2 0 0 1 0 10.8V1.2A1.2 1.2 0 0 1 1.2 0zm.3 1.5v8h5v-8zM4 10.2a.6.6 0 1 0 0 1.2.6.6 0 0 0 0-1.2z"/></svg>
          <span>+49 170 9876543</span>
        </div>
      </div>

      <div class="contact__group">
        <div class="contact__row">
          <svg class="contact__icon" viewBox="0 0 10 10"><circle cx="5" cy="5" r="4.3" fill="none" stroke="#22262e" stroke-width="1.2"/><path d="M.7 5h8.6M5 .7c-2.4 2.6-2.4 6 0 8.6M5 .7c2.4 2.6 2.4 6 0 8.6" fill="none" stroke="#22262e" stroke-width="1"/></svg>
          <span>www.kfnovum.com</span>
        </div>
        <div class="contact__row">
          <svg class="contact__icon" viewBox="0 0 10 8"><path d="M0 0h10v8H0z"/><path d="M0 0l5 4.3L10 0" fill="none" stroke="#fff" stroke-width="0.9"/></svg>
          <span>info@kfnovum.com</span>
        </div>
      </div>
    </address>

    <div class="fold-mark" style="top:392px"></div>
    <div class="fold-mark" style="top:556px"></div>
    <div class="fold-mark" style="top:786px"></div>

    <div class="side-rule side-rule--foot"></div>
    <div class="bank">
      <div>Bankverbindung:</div>
      <div>Musterbank Musterstadt</div>
      <div class="bank__codes">
        <div><span class="bank__label">IBAN</span>DE 123 456 789 1011 1213</div>
        <div><span class="bank__label">BIC</span>XXXXXXXXXXX</div>
      </div>
    </div>
  </main>
</body>
</html>
```